My wife is a classical pianist and she is organising a tango event. This will consist of her playing piano, a singer, a saxophonist and 2 tango dancers. I want the flyer to capture the colour, vibrancy of tango. Details to be included on the flyer are below.

I need the final design to be in psd so can change words and move things about if necessary and also change the flyer for future events. I don't want you to use the image attached but this gives an idea of tango. I need the flyer in portrait.

The Heart of Milonga
A night of Tango music and dance.

Date: 16th of November [url removed, login to view] pm

Venue: Carrow Hall. 17 Fenwick Row London, N4 2QB
Nearest Tubes: Holbeck Lane Station. Eastgate Line

Performers: Lina Voretti ( soprano)
Gianluca Bertolazzi- Morales ( sax)
Corinne Valdemar ( piano)

Dancers: Renato da Silveira
Noemie

Music by Ettore Balzani, Iván Malvedo, Tomas Quiroga, Julio Benvar, Fermin Lozada, Corinne Valdemar.

Tickets: £15 conc. £10
Tickets on the door or online
For more information
[url removed, login to view]
01632960418

```html
<!DOCTYPE html>
<html lang="en">
<head>
<meta charset="utf-8">
<title>The Heart of Milonga – A Night of Tango Music &amp; Dance</title>
<link rel="stylesheet" href="https://fonts.googleapis.com/css2?family=Signika:wght@600&family=Ubuntu:wght@500;700&display=swap">
<style>
  :root {
    --bg-top: #e0672d;
    --bg-mid: #e59a2c;
    --bg-bottom: #dcc21f;
    --ink-white: #ffffff;
    --title-red: #9c1418;
    --title-deep: #5a0a0c;
    --title-outline: #ffffff;
    --subtitle-ink: #1a0606;
    --art-ink: rgba(70, 22, 4, 0.55);
    --art-mid: rgba(110, 40, 10, 0.32);
    --art-edge: rgba(140, 60, 15, 0.12);
  }
  * { margin: 0; padding: 0; box-sizing: border-box; }
  html, body { width: 846px; height: 1200px; overflow: hidden; }
  body { background: #f3e9d9; }

  .flyer {
    position: relative;
    width: 846px;
    height: 1200px;
    overflow: hidden;
    background:
      repeating-linear-gradient(0deg, rgba(0,0,0,0.035) 0 2px, transparent 2px 5px),
      repeating-linear-gradient(90deg, rgba(255,255,255,0.04) 0 2px, transparent 2px 5px),
      linear-gradient(180deg, var(--bg-top) 0%, var(--bg-mid) 55%, var(--bg-bottom) 100%);
  }

  .dancers-art {
    position: absolute;
    left: 290px;
    top: 40px;
    width: 550px;
    height: 1120px;
    border-radius: 46% 42% 20% 30% / 30% 28% 14% 18%;
    background:
      radial-gradient(ellipse 30% 22% at 58% 22%, var(--art-ink) 0%, transparent 100%),
      radial-gradient(ellipse 45% 30% at 52% 45%, var(--art-mid) 0%, transparent 100%),
      linear-gradient(180deg, var(--art-mid) 0%, var(--art-edge) 70%, transparent 100%);
  }

  .details {
    position: absolute;
    left: 0;
    top: 30px;
    width: 400px;
    font-family: "Signika", "Trebuchet MS", sans-serif;
    font-weight: 600;
    color: var(--ink-white);
    text-transform: uppercase;
    text-shadow: 0 1px 2px rgba(80, 20, 0, 0.35);
  }
  .info-block { margin-bottom: 17px; }
  .info-heading {
    font-size: 20px;
    line-height: 24px;
    padding-left: 31px;
  }
  .info-lines {
    position: relative;
    font-size: 17px;
    line-height: 23px;
    letter-spacing: 0.3px;
    padding-left: 31px;
  }
  .info-lines::before {
    content: "";
    position: absolute;
    left: 0;
    top: 8px;
    border-top: 8px solid transparent;
    border-bottom: 8px solid transparent;
    border-left: 14px solid var(--ink-white);
  }
  .info-lines span { display: block; }

  .event-title {
    position: absolute;
    left: 0;
    top: 840px;
    width: 846px;
    height: 360px;
  }
  .title-svg { width: 846px; height: 360px; display: block; }
  .title-svg text { paint-order: stroke fill; stroke-linejoin: round; }
  .kicker {
    font-family: "Ubuntu", sans-serif;
    font-weight: 700;
    font-size: 52px;
    fill: var(--title-red);
    stroke: var(--title-outline);
    stroke-width: 4px;
  }
  .headline {
    font-family: "Ubuntu", sans-serif;
    font-weight: 500;
    font-size: 268px;
    fill: url(#titleFill);
    stroke: var(--title-outline);
    stroke-width: 7px;
  }
  .tagline {
    font-family: "Ubuntu", sans-serif;
    font-weight: 700;
    font-size: 30px;
    fill: var(--subtitle-ink);
    stroke: var(--title-outline);
    stroke-width: 4px;
  }
</style>
</head>
<body>
<main class="flyer">
  <div class="dancers-art" role="img" aria-label="Line illustration of a couple dancing the tango in a close embrace"></div>

  <section class="details">
    <div class="info-block">
      <h2 class="info-heading">Performers:</h2>
      <p class="info-lines">
        <span>Lina Voretti ( soprano)</span>
        <span>Gianluca Bertolazzi- Morales ( sax)</span>
        <span>Corinne Valdemar ( piano)</span>
      </p>
    </div>
    <div class="info-block">
      <h2 class="info-heading">Music by:</h2>
      <p class="info-lines">
        <span>Ettore Balzani, Iván Malvedo,</span>
        <span>Tomas Quiroga, Julio Benvar,</span>
        <span>Fermin Lozada, Corinne Valdemar.</span>
      </p>
    </div>
    <div class="info-block">
      <h2 class="info-heading">Dancers:</h2>
      <p class="info-lines">
        <span>Renato da Silveira</span>
        <span>Noemie</span>
      </p>
    </div>
    <div class="info-block">
      <h2 class="info-heading">Date:</h2>
      <p class="info-lines">
        <span>16th of November</span>
        <span>7.30 pm</span>
      </p>
    </div>
    <div class="info-block">
      <h2 class="info-heading">Venue:</h2>
      <p class="info-lines">
        <span>Carrow Hall.</span>
        <span>17 Fenwick Row London,</span>
        <span>N4 2QB Nearest Tubes:</span>
        <span>Holbeck Lane Station.</span>
        <span>Eastgate Line</span>
      </p>
    </div>
    <div class="info-block">
      <h2 class="info-heading">Tickets:</h2>
      <p class="info-lines">
        <span>£15 conc. £10</span>
        <span>Tickets on the door or online</span>
        <span>For more information</span>
        <span>www.corinnevaldemar.com</span>
        <span>01632960418</span>
      </p>
    </div>
  </section>

  <header class="event-title">
    <svg class="title-svg" viewBox="0 0 846 360" aria-label="The Heart of Milonga – A night of tango music and dance">
      <defs>
        <linearGradient id="titleFill" x1="0" y1="0" x2="1" y2="1">
          <stop offset="0" stop-color="var(--title-deep)"/>
          <stop offset="0.5" stop-color="var(--title-red)"/>
          <stop offset="1" stop-color="var(--title-deep)"/>
        </linearGradient>
      </defs>
      <text class="kicker" x="215" y="36">THE HEART OF</text>
      <text class="headline" x="14" y="248" textLength="818" lengthAdjust="spacingAndGlyphs">Milonga</text>
      <text class="tagline" x="58" y="292">A NIGHT OF TANGO MUSIC</text>
      <text class="tagline" x="660" y="292">&amp; DANCE.</text>
    </svg>
  </header>
</main>
</body>
</html>
```